Tidewell Private Yacht Charter "Rack Flyer"

This will be a 4" x 9" Rack flyer that is 4 colors and two sided. This is a Private Yacht charter company that is based in St Thomas, U.S. Virgin Islands. Our main product that I would like to promote on one entire side of the flyer is our Private Luxury Full Day "Glimmer Feast". our charter company is unique in the fact we offer customizable itineraries and we offer unique activities that keep the family and groups engaged in fun for the entire day. We would like something with our colors.

Target Market(s)

We are trying to reach an upscale clients that are looking for a Luxury Day Charter experience. these people will be most likely staying in Private Villas or staying at the Halvern Crest or QP Delacourt.

Requirements
Must have
• Contact Information:
Ph: (340) 555-0187
email: Info@tidewellvi.example
www.tidewellvi.example
One side should Promote our Glimmer Feast (Glimmer Feast is a trademarked name).
All Guests will receive "Welcome Mimosas"
> Up to 12 guests
> Full Brunch Spread to include, Assorted fruit tower, Artesian Waffle Board, Frittata's, Loaded Avocado Toast or an All American Breakfast.
> Specialty Cocktails with Bottle Service options available
List all of our Unique activities to include:
Snorkeling
Underwater WaveGlider
Cliff Diving
Paddleboarding
Towable Activities
TEXT TO BE WRITTEN:
Experience yacht charter service at its Finest!
Sail away with us on a Luxury Charter experience complete with a full brunch spread. During our sail we will take you to the hottest destination spots in the Caribbean surrounding St Thomas and St John. Warm, fresh baked afternoon cookies will be served on the way back from our days journeys. Unlimited water, sodas, beer and rum punch will be provided for the entire group to enjoy throughout the day.
_________________

On side two of the brochure you can refer to the downloaded text. We do not want pricing listed on the flyer

```html
<!DOCTYPE html>
<html lang="en">
<head>
<meta charset="utf-8">
<title>Tidewell Private Yacht Charter – Glimmer Feast Rack Flyer</title>
<link href="https://fonts.googleapis.com/css2?family=Caudex:ital,wght@0,700;1,700&family=Pinyon+Script&family=Quicksand:wght@500;600&display=swap" rel="stylesheet">
<style>
  :root{
    --navy:#1f3d8c;
    --red:#d1262c;
    --white:#ffffff;
    --sea-deep:#2d8fc0;
    --sea-light:#7cc6e4;
    --sand:#e9d3a6;
    --foam:#dfe9ef;
    --foam-blue:#c4d8e6;
  }
  html,body{margin:0;padding:0;width:1200px;height:2700px;overflow:hidden;background:var(--white);}
  .flyer{position:relative;width:1200px;height:2700px;overflow:hidden;font-family:"Quicksand",sans-serif;color:var(--navy);}
  .fill{position:absolute;}

  .hero-photo{left:0;top:0;width:1200px;height:703px;
    background:linear-gradient(180deg,#c9d8e0 0%,#e2cc9c 14%,#dcc08a 26%,var(--sea-light) 42%,var(--sea-deep) 100%);}
  .hero-title{position:absolute;left:40px;top:52px;margin:0;font-family:"Caudex",serif;font-weight:700;
    font-size:72px;color:var(--red);letter-spacing:-1px;text-shadow:2px 3px 4px rgba(0,0,0,.35);white-space:nowrap;}
  .product-name{position:absolute;margin:0;font-family:"Pinyon Script",cursive;font-weight:400;color:var(--white);
    font-size:184px;line-height:1;text-shadow:3px 4px 6px rgba(0,0,0,.45);}
  .product-name.line-one{left:50px;top:196px;}
  .product-name.line-two{left:205px;top:396px;}

  .brand-box{position:absolute;left:741px;top:594px;width:459px;height:109px;background:var(--white);
    display:flex;flex-direction:column;align-items:center;justify-content:center;gap:4px;}
  .brand-line{display:flex;align-items:center;gap:12px;}
  .brand-dot{width:16px;height:16px;border-radius:50%;background:var(--red);}
  .brand-name{font-weight:600;font-size:40px;line-height:44px;color:var(--red);}
  .contact{margin:0;font-weight:600;font-size:17px;line-height:21px;color:var(--navy);text-align:center;white-space:nowrap;}

  .headline{position:absolute;left:36px;top:712px;margin:0;font-weight:600;font-size:51px;color:var(--red);white-space:nowrap;letter-spacing:.6px;}

  .intro-bg{left:0;top:787px;width:1200px;height:648px;
    background:radial-gradient(ellipse at 70% 30%,#f2f6f8 0%,var(--foam) 45%,var(--foam-blue) 100%);}
  .guests-photo{left:0;top:787px;width:372px;height:598px;
    background:linear-gradient(160deg,#d7e3ea 0%,#c79f78 45%,#a36a3e 80%,#8a5532 100%);}
  .intro-copy{position:absolute;left:396px;top:796px;width:800px;margin:0;font-weight:500;font-size:41px;line-height:50px;letter-spacing:1.2px;white-space:nowrap;}

  .band{position:absolute;left:0;width:1200px;background:var(--white);}
  .band-welcome{top:1435px;height:83px;}
  .welcome{position:absolute;left:36px;top:1444px;margin:0;font-weight:600;font-size:48px;color:var(--red);letter-spacing:.6px;white-space:nowrap;}

  .shore-bg{left:0;top:1518px;width:1200px;height:1182px;
    background:linear-gradient(115deg,var(--foam-blue) 0%,var(--foam) 30%,#e6dcc6 55%,var(--sand) 75%,#dfc493 100%);}

  .menu{position:absolute;left:36px;top:1526px;margin:0;padding:0;list-style:none;font-weight:500;font-size:42px;letter-spacing:1.4px;}
  .menu li{line-height:50px;margin-bottom:23px;display:flex;align-items:flex-start;white-space:nowrap;}
  .menu .bullet::before{content:"";display:inline-block;width:16px;height:16px;border-radius:50%;background:var(--navy);margin:17px 34px 0 8px;flex:none;}
  .menu .wrap span{display:block;}
  .menu .wrap span + span{padding-left:6px;}
  .cocktails{position:absolute;left:36px;top:2094px;width:500px;margin:0;font-weight:500;font-size:42px;line-height:50px;letter-spacing:1.4px;}

  .snorkel-photo{left:538px;top:2000px;width:662px;height:490px;
    background:linear-gradient(180deg,#5fb7c9 0%,#3e8fa3 50%,#2c6d80 100%);}
  .activities-box{position:absolute;left:0;top:2362px;width:538px;height:128px;background:var(--white);}
  .activities-title{position:absolute;left:36px;top:2362px;margin:0;font-weight:600;font-size:49px;line-height:56px;color:var(--red);letter-spacing:1px;}
  .activities{position:absolute;top:2494px;margin:0;padding:0;list-style:none;font-weight:500;font-size:42px;line-height:50px;letter-spacing:1.4px;white-space:nowrap;}
  .activities.col-one{left:32px;}
  .activities.col-two{left:622px;top:2544px;}
</style>
</head>
<body>
<main class="flyer">
  <div class="fill hero-photo" role="img" aria-label="Catamaran anchored off a sandy beach in turquoise water, a child jumping from the stern"></div>
  <h1 class="hero-title">Private Luxury Full day Charter</h1>
  <p class="product-name line-one">Glimmer</p>
  <p class="product-name line-two">Feast</p>
  <div class="brand-box">
    <div class="brand-line"><span class="brand-dot"></span><span class="brand-name">Tidewell</span></div>
    <p class="contact">Ph: (340) 555-0187 · Info@tidewellvi.example<br>www.tidewellvi.example</p>
  </div>

  <h2 class="headline">Experience yacht charter service at its Finest!</h2>

  <div class="fill intro-bg" role="img" aria-label="Soft sea foam texture"></div>
  <div class="fill guests-photo" role="img" aria-label="Couple toasting with cocktails at a table of fresh fruit on deck"></div>
  <p class="intro-copy">Sail away with us on a Luxury Charter<br>experience complete with a full<br>brunch spread. During our sail we will<br>take you to the hottest destination<br>spots in the Caribbean surrounding<br>St Thomas and St John.<br>Warm, fresh baked afternoon cookies<br>will be served on the way back from<br>our days journeys. Unlimited water,<br>sodas, beer and rum punch will be<br>provided for the entire group to<br>enjoy throughout the day.</p>

  <div class="band band-welcome"></div>
  <h2 class="welcome">All Guests will receive “Welcome Mimosas”</h2>

  <div class="fill shore-bg" role="img" aria-label="Waves washing over a sandy shoreline"></div>
  <ul class="menu">
    <li class="bullet">Up to 12 guests</li>
    <li>Full Brunch Spread to include:</li>
    <li class="bullet">Assorted fruit tower</li>
    <li class="bullet">Artesian Waffle Board</li>
    <li class="bullet">Frittata’s</li>
    <li class="bullet">Loaded Avocado Toast or</li>
    <li class="bullet wrap"><div><span>an All American</span><span>Breakfast</span></div></li>
  </ul>
  <p class="cocktails">Specialty Cocktails with<br>Bottle Service options<br>available</p>

  <div class="fill snorkel-photo" role="img" aria-label="Two snorkelers in masks underwater"></div>
  <div class="activities-box"></div>
  <h2 class="activities-title">Unique activities<br>include:</h2>
  <ul class="activities col-one">
    <li>Snorkeling</li>
    <li>Underwater WaveGlider</li>
    <li>Cliff Diving</li>
  </ul>
  <ul class="activities col-two">
    <li>Paddleboarding</li>
    <li>Towable Activities</li>
  </ul>
</main>
</body>
</html>
```